Design for an exciting tech startup! Brochure+Letter Design Project

We're a startup called tasklyne with Phase 1 of a super exciting Remote Desk Steward software and app launching this October (tasklyne.net)

While we've got some basic items such as the corporate identity and website locked down, we're still lacking the essential little communication items that potential customers will be receiving from us.

We need a designer who can bring out a consistency into our stationery both on the online and offline items. We'd also like a recommended graphic style to represent the visuals that will be shown, especially in our user manual eg. icon-based OR flow chart style etc.

The list is as below. We're looking for templates here as the final items will be laid out at a later stage only when all contents are finalised.

1. A4 horizontal, 4-page brochure template
- circulated in PDF
- also allocate space for 2 equal size images per page
- page 1 with a prominent header, page 4 with a prominent footer
- to provide files in AI or PSD format
2. A4 horizontal, 20 page User Manual
- circulated in PDF
- also allocate space for 1 large image and 1 small image per page
3. Electronic direct mailer template
- for maximum of 200 words
4. A4 vertical, Letterhead template
- used in PDF form (potentially for press releases)
- prominent footer

If you are interested, please email us to receive these items:
1. Corporate Identity sheet on logo usage
2. E-direct mailer content

Good luck and enjoy your mission!

Dear Designers,

This project is mainly a brochure template + adaptation of this template's design to letterhead and electronic mailer.

We've made the brief more precise in case it has caused any misunderstanding and inconveniences to anyone.

Our brand identity items have also been uploaded for your reference.

Good luck!

Target Market(s)

HR and IT managers who will subscribe to the software on behalf of their companies, also bosses of Small Medium enterprises.

Industry/Entity Type

Communication

Requirements
Must have
• We only use these fonts:
Century Gothic
Arial

Currently, our preferred colours are blue and silver though we would not want to be restricted by strictly following these 2 colours.

```html
<!DOCTYPE html>
<html lang="en">
<head>
<meta charset="utf-8">
<title>tasklyne – Brochure Page</title>
<link href="https://fonts.googleapis.com/css2?family=Arimo:ital,wght@0,400;0,700;1,700&display=swap" rel="stylesheet">
<style>
  :root {
    --brand-blue: #1a5f95;
    --deep-blue: #1d4f7a;
    --accent-blue: #2f9ad8;
    --band-blue: #dcedf9;
    --badge-blue: #1b6aa9;
    --text-grey: #555a60;
    --sky-top: #cfe4f5;
    --sky-bottom: #ffffff;
    --photo-grey: #d8dadc;
  }
  * { margin: 0; padding: 0; box-sizing: border-box; }
  html, body { width: 1200px; height: 901px; overflow: hidden; background: #fff; }
  body { font-family: "Arimo", Arial, sans-serif; color: var(--text-grey); position: relative; }

  .sky {
    position: absolute; left: 0; top: 0; width: 1200px; height: 198px;
    background: linear-gradient(180deg, var(--sky-top) 0%, #e6f1fa 55%, var(--sky-bottom) 100%);
  }
  .hero-cubes {
    position: absolute; left: 26px; top: 36px; width: 180px; height: 140px;
    background: radial-gradient(ellipse at center, #f4f8fb 0%, #dfe9f1 60%, rgba(223,233,241,0) 100%);
  }
  .brand {
    position: absolute; right: 28px; top: 54px;
    font-size: 44px; font-weight: 400; color: var(--brand-blue); letter-spacing: -0.5px;
  }

  .title-band {
    position: absolute; left: 0; top: 198px; width: 1200px; height: 77px;
    background: var(--band-blue);
  }
  .title-band h1 {
    position: absolute; left: 28px; top: 20px;
    font-size: 31px; font-weight: 400; color: var(--deep-blue);
  }

  .copy { font-size: 15.5px; line-height: 25.4px; text-align: justify; }
  .copy em { font-style: italic; font-weight: 700; color: var(--accent-blue); }
  .intro { position: absolute; left: 28px; top: 293px; width: 766px; }
  .detail { position: absolute; left: 28px; top: 498px; width: 1144px; }

  .office-photo {
    position: absolute; left: 813px; top: 295px; width: 359px; height: 172px;
    border: 1px solid #8a9aa8;
    background: linear-gradient(90deg, #eceeef 0%, var(--photo-grey) 55%, #f2f3f4 100%);
  }

  .launch { position: absolute; left: 0; top: 648px; width: 1200px; text-align: center; color: var(--deep-blue); }
  .launch h2 { font-size: 31px; font-weight: 400; }
  .launch p { font-size: 18px; margin-top: 6px; }

  .store-badge {
    position: absolute; top: 740px; width: 202px; height: 58px;
    background: linear-gradient(180deg, #2b80c0 0%, var(--badge-blue) 100%);
    border-radius: 3px;
  }
  .store-badge.first { left: 392px; }
  .store-badge.second { left: 604px; }

  .footer-rule {
    position: absolute; left: 28px; top: 876px; width: 1144px; height: 2px; background: var(--brand-blue);
  }
  .address {
    position: absolute; left: 28px; top: 850px;
    font-size: 14.5px; letter-spacing: 1px; color: #5c6168;
  }
  .web-tab { position: absolute; left: 888px; top: 843px; width: 284px; height: 35px; }
  .web-tab span {
    position: absolute; left: 30px; top: 8px; width: 250px; text-align: center;
    font-size: 17px; letter-spacing: 2.5px; color: #fff;
  }
</style>
</head>
<body>
  <div class="sky" role="img" aria-label="Soft blue sky with light clouds"></div>
  <div class="hero-cubes" role="img" aria-label="Three white floating cubes"></div>
  <div class="brand">tasklyne</div>

  <header class="title-band">
    <h1>LOREM IPSUM - is simply dummy text</h1>
  </header>

  <p class="copy intro">Lorem Ipsum is simply dummy text of the printing and typesetting industry. Lorem Ipsum has been the industry's <em>standard dummy</em> text ever since the 1500s, when an unknown printer took a galley of type and scrambled it to make a type specimen book. It has survived not only five centuries, but also the leap into electronic typesetting, remaining essentially unchanged. It was popularised in the 1960s with the release of Markwell sheets containing Lorem Ipsum passages, and more recently with desktop publishing software like Quillset Pagemaster including versions of Lorem Ipsum. Markwell sheets containing Lorem Ipsum passages, and more recently with desktop.</p>

  <div class="office-photo" role="img" aria-label="Silhouette of a person working at a computer desk in front of office buildings"></div>

  <p class="copy detail">Lorem Ipsum is simply dummy text of the printing and typesetting industry. Lorem Ipsum has been the industry's standard dummy text ever since the 1500s, when an unknown printer took a galley of type and <em>scrambled</em> it to make a type specimen book. It has survived not only five centuries, but also the leap into electronic typesetting, remaining essentially unchanged. It was popularised in the 1960s with the release of Markwell sheets containing Lorem Ipsum passages, and more recently with desktop publishing software like <em>Quillset Pagemaster</em> including versions of Lorem Ipsum. Markwell sheets containing Lorem Ipsum passages, and more recently with desktop.</p>

  <section class="launch">
    <h2>Available Fall 2012</h2>
    <p>Leave, Travel Authorisation, Expense &amp; Attendance Management, Knowledge &amp; Collaboration capabilities</p>
  </section>

  <div class="store-badge first" role="img" aria-label="App store listing badge"></div>
  <div class="store-badge second" role="img" aria-label="App store listing badge"></div>

  <footer>
    <p class="address">Unit 4, Floor 12, Harbourline Tech Centre, 58 Meridian Road, Eastgate Business Park, Lindenport 40211</p>
    <div class="footer-rule"></div>
    <div class="web-tab">
      <svg width="284" height="35" viewBox="0 0 284 35">
        <defs>
          <linearGradient id="tabFill" x1="0" y1="0" x2="1" y2="0">
            <stop offset="0" stop-color="#1a5f95"/>
            <stop offset="1" stop-color="#2f9ad8"/>
          </linearGradient>
        </defs>
        <polygon points="22,0 284,0 284,35 0,35" fill="url(#tabFill)"/>
      </svg>
      <span>www.tasklyne.net</span>
    </div>
  </footer>
</body>
</html>
```